Vql Centres website for a maxillofacial surgery clinic

It's a website for a clinic for maxillofacial surgery in WordPress . The website doesn't need to be complicated but has to look professional. It needs to be in Dutch so i can give the texts. Similar websites are www.tandartsenpraktijkvoorn.example or www.brekspecialisten.example. Pages would be sort of similar to https://hetcentrumvoorgelaatzorg.example/ or https://veldhovenclinics.example/. Those lasts are maxillofacial surgery clinic websites, but there are little more extensive.
I uploaded the logo. If this is not the proper quality i can upload the eps. Logo was made through artbazaar.

Target Market(s)

Patients who can find me and see information about the clinic

Industry/Entity Type

Healthcare

Coding

Coded - Design and coding required

Number of Pages Required

5+ page

Font styles to use
Other font styles liked:
• Something standard professional

Colors
0054AA
0677BA
7BADD7
CADEEF
E8F1F8

Requirements
Nice to have
• Something in line with the logo. I prefer a little dark like the darker logos but I'm not sure if that's professional. Logos bgtor and wsvp are instances i'm registered to so they will have to be on the website too but small somewhere.

```html
<!DOCTYPE html>
<html lang="nl">
<head>
<meta charset="utf-8">
<title>Vql Centres – Kaakchirurgie</title>
<link href="https://fonts.googleapis.com/css2?family=Poppins:wght@400;500;600;700;800&display=swap" rel="stylesheet">
<style>
:root{
  --blue:#29a6e1;
  --blue-deep:#1d8fcb;
  --ink:#111111;
  --text:#333333;
  --muted:#666666;
  --slate:#5d7097;
  --footer:#6a7ea6;
  --card:#f2f2f2;
  --white:#ffffff;
  --photo-blue:#8cc3e6;
}
*{box-sizing:border-box;margin:0;padding:0}
html,body{width:1200px;height:3616px;overflow:hidden}
body{font-family:'Poppins',sans-serif;color:var(--text);background:var(--white);position:relative}
.abs{position:absolute}
section,header,footer,nav{position:absolute;left:0;width:1200px}

/* header */
.topbar{top:0;height:88px}
.brand{left:44px;top:22px;display:flex;align-items:center;gap:10px;font-weight:600;font-size:26px;color:var(--blue)}
.brand .dot{width:16px;height:16px;border-radius:50%;background:var(--blue)}
.contact-item{top:22px;display:flex;align-items:center;gap:8px;font-size:17px;color:var(--slate)}
.ring{width:50px;height:50px;border:3px solid var(--blue);border-radius:50%;display:flex;align-items:center;justify-content:center}

.mainnav{top:88px;height:49px;background:var(--blue)}
.mainnav a{position:absolute;top:16px;font-size:13.5px;color:var(--white);text-decoration:none}
.cta-nav{position:absolute;left:962px;top:12px;width:168px;height:26px;border-radius:13px;background:var(--slate);color:var(--white);font-size:12px;font-weight:500;text-align:center;line-height:26px}

/* hero */
.hero{top:137px;height:578px}
.hero-photo{position:absolute;inset:0 0 60px 0;background:linear-gradient(120deg,#2f3d5a 0%,#44506c 45%,#5a5566 70%,#2d3a60 100%)}
.hero h1{position:absolute;left:105px;top:135px;font-size:57px;line-height:66px;font-weight:700;color:var(--white)}
.hero p{position:absolute;left:105px;top:275px;width:500px;font-size:17.5px;line-height:22px;color:var(--white)}
.btn-pill{position:absolute;height:26px;border-radius:13px;background:var(--blue);color:var(--white);font-size:12px;text-align:center;line-height:26px}
.dots{position:absolute;top:523px;left:564px;display:flex;gap:17px}
.dots span{width:22px;height:22px;border-radius:50%;background:var(--blue)}
.dots span.ring-dot{background:transparent;border:2px solid var(--blue)}

/* headings */
.sec-title{position:absolute;left:0;width:1200px;text-align:center;font-size:29px;font-weight:700;color:var(--ink);letter-spacing:.3px}
.sec-sub{position:absolute;left:440px;width:360px;text-align:center;font-size:9.5px;line-height:12px;color:var(--text)}

/* treatments */
.treat-photo{position:absolute;width:210px;height:250px;border-radius:10px;background:linear-gradient(160deg,#a6d3ef,var(--photo-blue))}
.treat-name{position:absolute;font-size:16px;font-weight:600;color:var(--ink)}
.treat-text{position:absolute;width:205px;font-size:10px;line-height:12px;color:var(--text)}

/* blue bands */
.band{background:var(--blue)}
.band-photo{position:absolute;left:143px;top:55px;width:322px;height:322px;border-radius:50%;background:linear-gradient(135deg,#dfe8ee,#b9cbd8)}
.band h2{position:absolute;font-size:29px;font-weight:700;color:var(--white)}
.about-text{position:absolute;left:510px;width:525px;font-size:11.5px;line-height:14px;color:var(--white)}
.btn-slate{position:absolute;height:26px;border-radius:13px;background:var(--slate);color:var(--white);font-size:12px;text-align:center;line-height:26px}

/* reviews */
.review{position:absolute;top:1945px;width:256px;height:179px;background:var(--card)}
.stars{position:absolute;left:22px;top:14px;font-size:22px;letter-spacing:3px;color:var(--blue-deep)}
.review p{position:absolute;left:30px;top:52px;width:210px;font-size:10.5px;line-height:17px;color:var(--text)}
.avatar{position:absolute;left:28px;top:122px;width:38px;height:38px;border-radius:50%;background:linear-gradient(#1f6f9a,#7cc1e3)}
.rev-name{position:absolute;left:74px;top:123px;font-size:11px;font-weight:600;color:var(--ink)}
.rev-role{position:absolute;left:74px;top:140px;font-size:7.5px;color:var(--blue)}

/* clinic gallery */
.clinic-photo{position:absolute;top:156px;width:241px;height:198px;border-radius:6px;background:linear-gradient(135deg,#e6ecf0,#c9d5dd 60%,#d98a5a)}

/* team */
.member{position:absolute;top:2841px;width:190px;height:277px;border:1px solid #e6e6e6;border-radius:10px;background:var(--white)}
.member-photo{position:absolute;left:0;top:0;width:188px;height:212px;border-radius:10px 10px 0 0;background:linear-gradient(#eef1f4,#d7dde3)}
.socials{position:absolute;left:23px;top:200px;width:142px;height:28px;border-radius:14px;background:var(--blue);display:flex;justify-content:center;align-items:center;gap:12px}
.socials i{width:14px;height:14px;border-radius:50%;border:2px solid var(--white)}
.member h3{position:absolute;left:0;width:188px;top:238px;text-align:center;font-size:13.5px;font-weight:600;color:var(--ink)}
.member .role{position:absolute;left:0;width:188px;top:257px;text-align:center;font-size:9px;color:var(--blue)}

/* footer */
.site-footer{top:3210px;height:406px;background:var(--footer);color:var(--white)}
.foot-logo{position:absolute;left:58px;top:54px;width:166px;height:110px;background:var(--white);display:flex;align-items:center;justify-content:center;gap:8px;font-size:24px;font-weight:600;color:var(--blue)}
.foot-logo .dot{width:14px;height:14px;border-radius:50%;background:var(--blue)}
.foot-about{position:absolute;left:58px;top:190px;width:290px;font-size:13.5px;line-height:23px}
.foot-head{position:absolute;top:64px;font-size:16px;color:var(--blue)}
.foot-list{position:absolute;list-style:none;font-size:15px}
.foot-list li{position:relative;height:37.5px;padding-left:23px}
.foot-list li::before{content:"›";position:absolute;left:0;top:-2px;color:var(--blue);font-size:16px}
.foot-list.caps li{font-size:14px}
.foot-line{position:absolute;left:851px;display:flex;gap:20px;font-size:14.5px}
.foot-line svg{flex:none;margin-top:3px}
.foot-phone{position:absolute;left:851px;top:172px;width:214px;height:50px;border-radius:25px;background:var(--blue);display:flex;align-items:center;justify-content:center;gap:8px;font-size:16px;font-weight:500}
.foot-rule{position:absolute;left:58px;top:330px;width:1105px;height:1px;background:rgba(255,255,255,.45)}
.foot-social{position:absolute;left:63px;top:365px;display:flex;gap:16px}
.foot-social i{width:12px;height:12px;border-radius:50%;background:var(--white)}
.copyright{position:absolute;right:37px;top:362px;font-size:12.5px}
</style>
</head>
<body>

<header class="topbar">
  <div class="abs brand"><span class="dot"></span>Vql Centres</div>
  <div class="abs contact-item" style="left:618px">
    <span class="ring"><svg width="22" height="22" viewBox="0 0 24 24"><path fill="#29a6e1" d="M6.6 10.8a15.1 15.1 0 0 0 6.6 6.6l2.2-2.2c.3-.3.7-.4 1-.2 1.1.4 2.3.6 3.6.6.6 0 1 .4 1 1V20c0 .6-.4 1-1 1A17 17 0 0 1 3 4c0-.6.4-1 1-1h3.5c.6 0 1 .4 1 1 0 1.3.2 2.5.6 3.6.1.3 0 .7-.2 1z"/></svg></span>
    +31 20 555 0147
  </div>
  <div class="abs contact-item" style="left:875px">
    <span class="ring"><svg width="22" height="22" viewBox="0 0 24 24"><path fill="#29a6e1" d="M3 6h18v12H3z"/><path fill="none" stroke="#fff" stroke-width="1.6" d="M3 7l9 6 9-6"/></svg></span>
    info@vqlcentres.example
  </div>
</header>

<nav class="mainnav">
  <a style="left:98px">Home</a>
  <a style="left:222px">Behandelingen</a>
  <a style="left:399px">Vergoeding</a>
  <a style="left:552px">Ons team</a>
  <a style="left:698px">Folders</a>
  <a style="left:833px">Contact</a>
  <span class="cta-nav">MAAK EEN AFSPRAAK</span>
</nav>

<section class="hero">
  <div class="hero-photo" role="img" aria-label="Tandarts in blauwe handschoenen behandelt een patiënt"></div>
  <svg class="abs" style="left:0;top:500px" width="1200" height="78" viewBox="0 0 1200 78">
    <path fill="#29a6e1" d="M0 0 L615 52 L1200 0 L1200 14 L615 78 L0 30 Z"/>
    <path fill="#ffffff" d="M0 30 L615 78 L1200 14 L1200 78 L0 78 Z"/>
  </svg>
  <h1>Welkom BIJ<br>Vql Centres</h1>
  <p>Lorem ipsum dolor sit amet, consectetur adipiscing elit, sed do eiusmod tempor incididunt ut labore et</p>
  <span class="btn-pill" style="left:105px;top:339px;width:105px">LEES MEER</span>
  <div class="dots"><span></span><span class="ring-dot"></span><span></span></div>
</section>

<section style="top:715px;height:614px">
  <h2 class="sec-title" style="top:52px">BEHANDELINGEN</h2>
  <p class="sec-sub" style="top:100px">Lorem ipsum dolor sit amet, consectetur adipiscing elit, sed do eiusmod tempor incididunt ut labore et dolore magna aliqua</p>
  <svg class="abs" style="left:135px;top:333px" width="36" height="58" viewBox="0 0 36 58"><path fill="none" stroke="#29a6e1" stroke-width="3" d="M33 2 L4 29 L33 56"/></svg>
  <svg class="abs" style="left:1000px;top:333px" width="36" height="58" viewBox="0 0 36 58"><path fill="none" stroke="#29a6e1" stroke-width="3" d="M3 2 L32 29 L3 56"/></svg>

  <div class="treat-photo" style="left:199px;top:206px" role="img" aria-label="Tandarts behandelt een patiënte"></div>
  <div class="treat-name" style="left:203px;top:477px">KAAKCHIRURGIE</div>
  <p class="treat-text" style="left:206px;top:500px">Lorem ipsum dolor sit amet, consec adipiscing elit, sed do eiusmod tempor incididunt ut labore et dolore magna aliqua</p>

  <div class="treat-photo" style="left:482px;top:206px" role="img" aria-label="Kaakchirurg met patiënt"></div>
  <div class="treat-name" style="left:491px;top:477px">VERWIJSPRAKTIJK</div>
  <p class="treat-text" style="left:489px;top:500px">Lorem ipsum dolor sit amet, consec adipiscing elit, sed do eiusmod tempor incididunt ut labore et dolore magna aliqua</p>

  <div class="treat-photo" style="left:764px;top:206px" role="img" aria-label="Tandarts onderzoekt een lachende patiënte"></div>
  <div class="treat-name" style="left:771px;top:477px">VERWIJZER</div>
  <p class="treat-text" style="left:773px;top:503px">Lorem ipsum dolor sit amet, consec adipiscing elit, sed do eiusmod tempor incididunt ut labore et dolore magna aliqua</p>
</section>

<section class="band" style="top:1329px;height:412px">
  <div class="band-photo" role="img" aria-label="Tandarts helpt een glimlachende patiënte"></div>
  <h2 style="left:505px;top:76px">OVER ONS</h2>
  <p class="about-text" style="top:125px">Lorem ipsum dolor sit amet, consectetur adipiscing elit, sed do eiusmod tempor incididunt ut labore et dolore magna aliqua Ut enim ad minim veniam.Lorem ipsum dolor sit amet, consectetur adipiscing elit, sed do eiusmod tempor incididunt ut labore et dolore magna aliqua Ut enim ad minim veniam</p>
  <p class="about-text" style="top:190px">Lorem ipsum dolor sit amet, consectetur adipiscing elit, sed do eiusmod tempor incididunt ut labore et dolore magna aliqua Ut enim ad minim veniam.Lorem ipsum dolor sit amet, consectetur adipiscing elit, sed do eiusmod tempor incididunt ut labore et dolore magna aliqua Ut enim ad minim veniam</p>
  <p class="about-text" style="top:255px">Lorem ipsum dolor sit amet, consectetur adipiscing elit, sed do eiusmod tempor incididunt ut labore et dolore magna aliqua Ut enim ad minim veniam.Lorem ipsum dolor sit amet, consectetur adipiscing elit, sed do eiusmod tempor incididunt ut labore et dolore magna aliqua Ut enim ad minim veniam</p>
  <span class="btn-slate" style="left:516px;top:334px;width:104px">LEES MEER</span>
</section>

<section style="top:1741px;height:500px">
  <h2 class="sec-title" style="top:88px;left:-8px">WHAT CLIENT SAYS</h2>
</section>
<div class="review" style="left:146px"><span class="stars">★★★★★</span><p>Interdum et malesuada fames ac ante ipsum primis in faucibus donec tempor nisi neque.</p><span class="avatar"></span><span class="rev-name">Lotte Verhaar</span><span class="rev-role">MANAGER</span></div>
<div class="review" style="left:459px"><span class="stars">★★★★★</span><p>Interdum et malesuada fames ac ante ipsum primis in faucibus donec tempor nisi neque.</p><span class="avatar"></span><span class="rev-name">Lotte Verhaar</span><span class="rev-role">MANAGER</span></div>
<div class="review" style="left:772px"><span class="stars">★★★★★</span><p>Interdum et malesuada fames ac ante ipsum primis in faucibus donec tempor nisi neque.</p><span class="avatar"></span><span class="rev-name">Lotte Verhaar</span><span class="rev-role">MANAGER</span></div>

<section class="band" style="top:2241px;height:414px">
  <h2 style="left:0;width:1180px;top:40px;text-align:center;line-height:38px">WELKOM IN ONS<br>MODERNE KLINIEK</h2>
  <div class="clinic-photo" style="left:88px" role="img" aria-label="Tandarts in gesprek met patiënte in behandelkamer"></div>
  <div class="clinic-photo" style="left:351px" role="img" aria-label="Behandelkamer met oranje stoel"></div>
  <div class="clinic-photo" style="left:614px;background:linear-gradient(135deg,#e3e6ea,#b8bcc6 55%,#4b3d62)" role="img" aria-label="Paarse behandelstoel"></div>
  <div class="clinic-photo" style="left:877px" role="img" aria-label="Lichte behandelkamer met monitor"></div>
</section>

<section style="top:2655px;height:555px">
  <h2 class="sec-title" style="top:66px;left:-14px">TEAM VAN PROFESSIONALS</h2>
</section>
<div class="member" style="left:140px"><div class="member-photo" role="img" aria-label="Portret teamlid"></div><div class="socials"><i></i><i></i><i></i></div><h3>Ruben Aalders</h3><span class="role">Founder &amp; CEO</span></div>
<div class="member" style="left:375px"><div class="member-photo" role="img" aria-label="Portret teamlid"></div><div class="socials"><i></i><i></i><i></i></div><h3>Ruben Aalders</h3><span class="role">Founder &amp; CEO</span></div>
<div class="member" style="left:620px"><div class="member-photo" role="img" aria-label="Portret teamlid"></div><div class="socials"><i></i><i></i><i></i></div><h3>Ruben Aalders</h3><span class="role">Founder &amp; CEO</span></div>
<div class="member" style="left:865px"><div class="member-photo" role="img" aria-label="Portret teamlid"></div><div class="socials"><i></i><i></i><i></i></div><h3>Ruben Aalders</h3><span class="role" style="color:#999">Founder &amp; CEO</span></div>

<footer class="site-footer">
  <div class="foot-logo"><span class="dot"></span>Vql Centres</div>
  <p class="foot-about">Lorem ipsum dolor sit amet, consectetur adipiscing elit, sed do eiusmod tempor incididunt ut labore et dolore</p>

  <div class="foot-head" style="left:413px">Snelle koppelingen</div>
  <ul class="foot-list" style="left:413px;top:106px">
    <li>Home</li><li>Behandelingen</li><li>Vergoeding</li><li>Ons team</li><li>Folders</li>
  </ul>

  <div class="foot-head" style="left:646px">Behandelingen</div>
  <ul class="foot-list caps" style="left:646px;top:106px">
    <li>KAAKCHIRURGIE</li><li>VERWIJSPRAKTIJK</li><li>VERWIJZER</li><li style="line-height:23px;height:46px">CHIRURGISCHE<br>ENDODONTIE</li>
  </ul>

  <div class="foot-head" style="left:851px">Een afspraak maken</div>
  <div class="foot-line" style="top:106px"><svg width="12" height="16" viewBox="0 0 12 16"><path fill="#29a6e1" d="M6 0a6 6 0 0 0-6 6c0 4.5 6 10 6 10s6-5.5 6-10a6 6 0 0 0-6-6zm0 8.5A2.5 2.5 0 1 1 6 3.5a2.5 2.5 0 0 1 0 5z"/></svg>Lindelaan 42, Amstelveen</div>
  <div class="foot-line" style="top:143px"><svg width="14" height="11" viewBox="0 0 14 11"><rect width="14" height="11" fill="#29a6e1"/><path d="M0 1l7 5 7-5" fill="none" stroke="#6a7ea6" stroke-width="1.4"/></svg>info@vqlcentres.example</div>
  <div class="foot-phone"><svg width="16" height="16" viewBox="0 0 24 24"><path fill="#fff" d="M6.6 10.8a15.1 15.1 0 0 0 6.6 6.6l2.2-2.2c.3-.3.7-.4 1-.2 1.1.4 2.3.6 3.6.6.6 0 1 .4 1 1V20c0 .6-.4 1-1 1A17 17 0 0 1 3 4c0-.6.4-1 1-1h3.5c.6 0 1 .4 1 1 0 1.3.2 2.5.6 3.6.1.3 0 .7-.2 1z"/></svg>(+31)20 555 0147</div>

  <div class="foot-rule"></div>
  <div class="foot-social"><i></i><i></i><i></i></div>
  <div class="copyright">Copyright © 2023. All Right Reserved.</div>
</footer>

</body>
</html>
```